you can visit www.brisa-tostada.com and www.instagram.com\brisatostada

www.nuevosendero.co
www.instagram.com\nsdv.co

combining this 2 business into one company website

### 1. **Home Page:**
- **Company Overview:** Briefly introduce Brisa Tostada, highlight your mission and values.
- **Navigation Menu:** Links to About Us, Events, Catering, Menu, and Contact Us.
- **Dynamic Banner:** Showcase specials, events, and new updates.

### 2. **About Us Page:**
- **History:** Share your story, how you started, and your journey.
- **Team:** Introduce your key team members with photos and bios.

### 3. **Events Page:**
- **Dynamic Calendar:** Integrate Google Calendar to showcase events and schedules.
- **Event Details:** Detailed descriptions of upcoming events with images and RSVP options.

### 4. **Catering Page:**
- **Booking Form:** A user-friendly form for booking catering services.
- **Packages & Pricing:** Clearly list your catering packages and pricing.
- **Testimonials:** Showcase positive reviews from previous clients.

### 5. **Menu Page:**
- **Online Order:** Embed or redirect to your Square online order menu for easy access.
- **Menu Sections:** Categorize your menu items (e.g., Appetizers, Main Course, Desserts).

### 6. **Contact Us Page:**
- **Contact Form:** Simple form for inquiries and feedback.
- **Location & Hours:** Display your location on Google Maps and list your operating hours.
- **Social Media Links:** Integrate links to your Instagram and other social platforms.

### 7. **Responsive Design:**
- Ensure the website is mobile-friendly and responsive on all devices.

### 8. **SEO Optimization:**
- Use relevant keywords and meta tags to improve search engine ranking. optimize seo and google analytics , google reviews embedded

### 9. **Social Media Integration:**
- Add social media icons that link directly to your Instagram and other platforms.

### 10. **Security:**
- Ensure your website has SSL certification

```html
<!DOCTYPE html>
<html lang="en">
<head>
<meta charset="utf-8">
<title>Brisa Tostada — Authentic Flavors, Catering &amp; Events</title>
<link rel="stylesheet" href="https://fonts.googleapis.com/css2?family=Archivo+Black&family=Poppins:wght@400;500;600;700&family=Yellowtail&display=swap">
<style>
:root{
  --red:#d71f26;
  --red-dark:#a8151b;
  --ink:#111111;
  --text:#555555;
  --muted:#888888;
  --dark:#1b1b1b;
  --wood:#2a2a2a;
  --white:#ffffff;
  --line:#e6e6e6;
}
*{box-sizing:border-box;margin:0;padding:0}
html,body{width:1200px;height:4528px;overflow:hidden}
body{position:relative;background:var(--white);font-family:"Poppins",sans-serif;color:var(--text)}
.abs{position:absolute}
.display{font-family:"Archivo Black",sans-serif;color:var(--ink);text-transform:uppercase;letter-spacing:-0.5px;line-height:1.15}
.display .hl{color:var(--red)}
.rule{position:absolute;height:3px;width:76px;background:var(--red)}
.copy{font-size:12.5px;line-height:22px;color:var(--text)}
.brush{position:absolute;display:flex;align-items:center;justify-content:center;font-family:"Yellowtail",cursive;color:var(--white);font-size:28px;text-decoration:none}
.brush svg{position:absolute;inset:0;width:100%;height:100%;z-index:0}
.brush span{position:relative;z-index:1}
.media{position:absolute}

/* header */
.site-header{position:absolute;left:0;top:0;width:1200px;height:73px;background:var(--white);box-shadow:0 2px 8px rgba(0,0,0,.06);z-index:5}
.logo-badge{position:absolute;left:90px;top:10px;width:107px;height:152px;background:var(--white);border:2px solid var(--red);box-shadow:0 3px 10px rgba(0,0,0,.15);display:flex;flex-direction:column;align-items:center;padding-top:14px;z-index:6}
.logo-badge .name{font-family:"Poppins",sans-serif;font-weight:700;font-size:12px;color:var(--ink);text-align:center;line-height:14px}
.logo-badge .dot{width:42px;height:42px;background:var(--red);margin-top:14px}
.logo-badge .seal{width:58px;height:34px;background:#ececec;margin-top:16px}
.main-nav{position:absolute;left:340px;top:28px;display:flex;gap:20px;font-size:11.5px;font-weight:500;color:var(--ink)}
.main-nav a{color:inherit;text-decoration:none}
.caret{font-size:8px;margin-left:3px}

/* hero */
.hero{position:absolute;left:0;top:73px;width:1200px;height:660px;background:radial-gradient(ellipse at 72% 45%,#5a3a2a 0%,#2a1f1a 35%,#151515 65%),#151515}
.hero-photo{position:absolute;inset:0;background:linear-gradient(180deg,rgba(230,90,20,.55) 0%,rgba(0,0,0,0) 18%,rgba(0,0,0,0) 80%,rgba(235,110,20,.6) 100%)}
.hero-title{position:absolute;left:126px;top:168px;font-size:80px;color:var(--white);line-height:82px}
.hero-title .hl{color:var(--red)}
.hero-sub{position:absolute;left:128px;top:414px;font-family:"Archivo Black",sans-serif;font-size:14px;color:var(--white);letter-spacing:.3px}

/* split sections */
.frame{position:absolute;border:3px solid var(--red)}

/* menu */
.menu-band{position:absolute;left:0;top:1775px;width:1200px;height:353px;background:linear-gradient(90deg,#1f1f1f,#2c2c2c 50%,#1f1f1f)}
.tabs{position:absolute;left:0;width:1200px;top:1904px;display:flex;justify-content:center;gap:18px;font-size:11px;font-weight:600;color:var(--white)}
.tabs .on{border-bottom:2px solid var(--red)}
.menu-card{position:absolute;top:1955px;width:242px;height:307px;background:var(--white);box-shadow:0 6px 18px rgba(0,0,0,.1)}
.menu-card .media{left:0;top:0;width:242px;height:172px}
.price{position:absolute;left:15px;top:157px;width:117px;height:28px;background:var(--red);color:var(--white);font-size:13px;font-weight:600;display:flex;align-items:center;justify-content:center}
.menu-card h3{position:absolute;left:17px;top:200px;font-family:"Archivo Black",sans-serif;font-size:14px;color:var(--ink)}
.menu-card p{position:absolute;left:17px;top:222px;width:210px;font-size:11px;line-height:19px;color:var(--muted)}

/* events */
.event-card{position:absolute;top:3118px;width:275px;height:319px;background:var(--white);box-shadow:0 6px 18px rgba(0,0,0,.08)}
.event-card .media{left:0;top:0;width:275px;height:192px}
.event-card h3{position:absolute;left:18px;top:210px;font-family:"Archivo Black",sans-serif;font-size:13.5px;color:var(--ink)}
.event-card .meta{position:absolute;left:18px;top:238px;font-size:9.5px;color:var(--muted);display:flex;gap:16px}
.event-card p{position:absolute;left:18px;top:260px;width:240px;font-size:11px;line-height:19px;color:var(--text)}

/* instagram */
.handle{position:absolute;left:154px;font-family:"Archivo Black",sans-serif;font-size:14px;color:var(--ink);display:flex;align-items:center;gap:10px}
.handle i{display:block;width:20px;height:20px;border:2px solid var(--red);border-radius:6px}

/* footer */
.site-footer{position:absolute;left:0;top:4125px;width:1200px;height:403px;background:var(--dark);color:#dddddd}
.site-footer h4{font-family:"Archivo Black",sans-serif;font-size:13.5px;color:var(--white);text-transform:uppercase;position:absolute}
.site-footer .item{position:absolute;font-size:11.5px;line-height:20px;color:#e8e8e8}
.site-footer .pin{color:var(--red)}
.social{position:absolute;top:4282px;left:634px;display:flex;gap:10px}
.social span{width:28px;height:28px;border-radius:50%;background:#2f2f2f}
.social span:first-child{background:var(--red)}
.pay{position:absolute;left:910px;top:4235px;display:grid;grid-template-columns:repeat(5,32px);gap:8px 8px}
.pay span{height:20px;background:#f2f2f2;border-radius:3px}
.foot-rule{position:absolute;left:90px;top:4460px;width:1020px;height:1px;background:#3a3a3a}
</style>
</head>
<body>

<header class="site-header">
  <nav class="main-nav">
    <a href="#">ABOUT US<span class="caret">▾</span></a>
    <a href="#">EVENTS<span class="caret">▾</span></a>
    <a href="#">CATERING<span class="caret">▾</span></a>
    <a href="#">MENU<span class="caret">▾</span></a>
    <a href="#">CONTACT US</a>
  </nav>
  <a class="brush" href="#" style="left:800px;top:14px;width:205px;height:46px;font-size:26px">
    <svg viewBox="0 0 205 46" preserveAspectRatio="none"><path d="M6 10 L196 4 L204 22 L194 42 L10 40 L0 24 Z" fill="#d71f26"/></svg><span>Order Now</span></a>
  <svg class="abs" style="left:1030px;top:24px" width="24" height="24" viewBox="0 0 24 24" fill="none" stroke="#111" stroke-width="2"><circle cx="12" cy="8" r="4.5"/><path d="M3 22c1-5 5-7 9-7s8 2 9 7"/></svg>
  <svg class="abs" style="left:1074px;top:24px" width="26" height="24" viewBox="0 0 26 24" fill="none" stroke="#111" stroke-width="2"><path d="M1 3h4l3 13h13l3-9H7"/><circle cx="10" cy="21" r="1.6"/><circle cx="19" cy="21" r="1.6"/></svg>
  <span class="abs" style="left:1094px;top:20px;width:12px;height:12px;border-radius:50%;background:var(--red);color:#fff;font-size:8px;text-align:center;line-height:12px">0</span>
</header>

<div class="logo-badge">
  <div class="name">Brisa<br>Tostada</div>
  <div class="dot"></div>
  <div class="seal"></div>
</div>

<section class="hero">
  <div class="hero-photo" role="img" aria-label="Grilled steak with onion rings on a dark plate over a charred wood background framed by flames"></div>
  <h1 class="display hero-title">Make<br><span class="hl">Your</span><br>Event</h1>
  <p class="hero-sub">FLAVORFUL BOOK CATERING TODAY!</p>
  <a class="brush" href="#" style="left:125px;top:457px;width:305px;height:50px">
    <svg viewBox="0 0 305 50" preserveAspectRatio="none"><path d="M4 14 L292 6 L305 26 L290 46 L14 44 L0 28 Z" fill="#d71f26"/></svg><span>Order Now</span></a>
  <span class="abs" style="left:1043px;top:490px;width:28px;height:28px;border:2px solid #fff;border-radius:50%"></span>
</section>

<!-- destination -->
<div class="frame" style="left:90px;top:848px;width:465px;height:424px"></div>
<div class="media" style="left:113px;top:840px;width:464px;height:415px;background:linear-gradient(135deg,#3b2618,#8a4a22 45%,#c9a063 70%,#2a1d14)" role="img" aria-label="Grilled ribs with fries and dipping sauce on a wooden board"></div>
<h2 class="display abs" style="left:622px;top:878px;font-size:28px">Your Destination For<br>Authentic <span class="hl">Flavors</span></h2>
<div class="rule" style="left:622px;top:966px"></div>
<p class="copy abs" style="left:622px;top:991px;width:488px">We're dedicated to bringing you authentic, handcrafted dishes that celebrate heritage and flavor. From golden-baked empanadas to delightful desserts, every item on our menu is made with love and the finest ingredients.</p>
<p class="copy abs" style="left:622px;top:1073px;width:488px">Whether you're stopping by for a quick bite, planning a grand event, or looking for catering services, we're here to create unforgettable experiences for every occasion.</p>
<a class="brush" href="#" style="left:622px;top:1165px;width:228px;height:50px">
  <svg viewBox="0 0 228 50" preserveAspectRatio="none"><path d="M6 12 L216 6 L228 26 L214 46 L12 44 L0 26 Z" fill="#d71f26"/></svg><span>Learn More</span></a>
<div class="media" style="left:1020px;top:1225px;width:170px;height:95px;background:radial-gradient(ellipse at center,#c82a22 0%,rgba(200,42,34,.25) 55%,rgba(255,255,255,0) 72%)" role="img" aria-label="Red chili pepper with scattered flakes"></div>

<!-- order online -->
<h2 class="display abs" style="left:88px;top:1380px;font-size:54px">Order <span class="hl">Online</span></h2>
<h3 class="display abs" style="left:90px;top:1450px;font-size:28px">And Enjoy Anywhere</h3>
<div class="rule" style="left:90px;top:1500px"></div>
<p class="copy abs" style="left:90px;top:1520px;width:470px">Craving something delicious? Place your order online for pickup or delivery and enjoy your favorites from the comfort of your home.</p>
<a class="brush" href="#" style="left:90px;top:1587px;width:222px;height:50px">
  <svg viewBox="0 0 222 50" preserveAspectRatio="none"><path d="M6 12 L210 6 L222 26 L208 46 L12 44 L0 26 Z" fill="#d71f26"/></svg><span>Order Now</span></a>
<div class="media" style="left:560px;top:1375px;width:575px;height:295px;background:radial-gradient(ellipse at 55% 50%,#6b3b22 0%,#b77a45 35%,#f0d24a 55%,rgba(255,255,255,0) 72%)" role="img" aria-label="Meat and vegetable skewers on a wooden board with sauce and spices"></div>

<!-- menu -->
<div class="menu-band" role="img" aria-label="Dark wooden plank background"></div>
<div class="media" style="left:0;top:1720px;width:155px;height:110px;background:radial-gradient(circle at 35% 65%,#e2362a 0 32%,rgba(0,0,0,0) 33%),radial-gradient(circle at 78% 30%,#e8452f 0 26%,rgba(0,0,0,0) 27%)" role="img" aria-label="Sliced tomato halves"></div>
<h2 class="display abs" style="left:0;width:1200px;text-align:center;top:1830px;font-size:28px;color:var(--white)">Discover The Menu</h2>
<div class="rule" style="left:562px;top:1876px"></div>
<div class="tabs"><span class="on">ALL</span><span>CRISPY GRILLED</span><span>RAMEN</span><span>CATERING</span><span>BAKED EMPANADA</span><span>FROZEN EMPANADA</span><span>BAKED PASTRIES</span></div>

<article class="menu-card" style="left:90px">
  <div class="media" style="background:linear-gradient(135deg,#8a3a18,#d87a3a 50%,#f3e2cf)" role="img" aria-label="Crispy pork belly being sliced"></div>
  <div class="price">CAD$15.25</div><h3>LECHON KAWALI</h3>
  <p>Grilled and Crispy pork combined seasoned with a blend of spices and...</p>
</article>
<article class="menu-card" style="left:349px">
  <div class="media" style="background:linear-gradient(135deg,#2d2d2d,#c9a56a 50%,#3a3a3a)" role="img" aria-label="Bowl of tonkotsu ramen with egg and chopsticks"></div>
  <div class="price">CAD$16.95</div><h3>TONKOTSU RAMEN</h3>
  <p>Indulge in the ultimate ramen experience with our classic TONKOT-SU...</p>
</article>
<article class="menu-card" style="left:609px">
  <div class="media" style="background:linear-gradient(135deg,#3e6b2a,#d38a3c 50%,#f4f1ec)" role="img" aria-label="Bowl of crispy fried pork pieces on green leaves"></div>
  <div class="price">CAD$40.00</div><h3>CRISPY PATA</h3>
  <p>Crispy Pata - Filipino Deep Fried Pork Hock Celebrate with the irresistible taste..</p>
</article>
<article class="menu-card" style="left:869px">
  <div class="media" style="background:linear-gradient(135deg,#c2322a,#eec06a 50%,#f6efe3)" role="img" aria-label="Golden baked empanadas on a plate"></div>
  <div class="price">CAD$5.00</div><h3>BAKED EMPANADA</h3>
  <p>Empanada is a flaky baked turnover in the shape of half-moon made with...</p>
</article>
<a class="brush" href="#" style="left:500px;top:2290px;width:202px;height:46px;font-size:26px">
  <svg viewBox="0 0 202 46" preserveAspectRatio="none"><path d="M6 10 L190 5 L202 24 L190 42 L12 41 L0 24 Z" fill="#d71f26"/></svg><span>Order Now</span></a>

<!-- occasion -->
<div class="frame" style="left:90px;top:2451px;width:465px;height:409px"></div>
<div class="media" style="left:113px;top:2443px;width:464px;height:415px;background:linear-gradient(135deg,#2a2420,#7a6656 45%,#c9b8a6 70%,#1e1a18)" role="img" aria-label="Friends celebrating on a sofa with balloons"></div>
<h2 class="display abs" style="left:622px;top:2462px;font-size:28px">Make Every Occasion<br><span class="hl">Special</span></h2>
<p class="copy abs" style="left:622px;top:2574px;width:490px">Planning an event? Let us handle the food while you enjoy the celebration. Our catering services are perfect for:</p>
<p class="copy abs" style="left:622px;top:2622px;width:490px">Corporate Events<br>Weddings<br><b style="color:var(--ink)">Birthday:</b><br>Family Gatherings</p>
<p class="copy abs" style="left:622px;top:2715px;width:490px">With flexible packages and a focus on quality, we'll make your event unforgettable.</p>
<a class="brush" href="#" style="left:622px;top:2785px;width:226px;height:50px">
  <svg viewBox="0 0 226 50" preserveAspectRatio="none"><path d="M6 12 L214 6 L226 26 L212 46 L12 44 L0 26 Z" fill="#d71f26"/></svg><span>Book Catering</span></a>

<!-- events -->
<h2 class="display abs" style="left:0;width:1200px;text-align:center;top:2978px;font-size:28px">Upcoming Events &amp; <span class="hl">Specials</span></h2>
<p class="copy abs" style="left:300px;width:600px;text-align:center;top:3046px">There's always something happening! Check out our event calendar for the latest pop-ups, live music nights, and seasonal specials.</p>
<article class="event-card" style="left:168px">
  <div class="media" style="background:linear-gradient(135deg,#4a3a30,#a08670 50%,#d9cfc4)" role="img" aria-label="Group gathered around an outdoor grill"></div>
  <h3>SOME BLOG HERE</h3><div class="meta"><span>▢ 25-05-2023</span><span>● By John</span></div>
  <p>Lorem Ipsum simply printing typesetting industry lorem Ipsum...</p>
</article>
<article class="event-card" style="left:462px">
  <div class="media" style="background:linear-gradient(135deg,#5b6a3a,#b08a5a 50%,#e2d2bb)" role="img" aria-label="Friends at a backyard barbecue table"></div>
  <h3>SOME BLOG HERE</h3><div class="meta"><span>▢ 25-05-2023</span><span>● By John</span></div>
  <p>Lorem Ipsum simply printing typesetting industry lorem Ipsum...</p>
</article>
<article class="event-card" style="left:755px">
  <div class="media" style="background:linear-gradient(135deg,#3a4a66,#a06a5a 50%,#d8c8be)" role="img" aria-label="Guests sharing food at an outdoor event"></div>
  <h3>SOME BLOG HERE</h3><div class="meta"><span>▢ 25-05-2023</span><span>● By John</span></div>
  <p>Lorem Ipsum simply printing typesetting industry lorem Ipsum...</p>
</article>
<a class="brush" href="#" style="left:480px;top:3468px;width:228px;height:50px">
  <svg viewBox="0 0 228 50" preserveAspectRatio="none"><path d="M6 12 L216 6 L228 26 L214 46 L12 44 L0 26 Z" fill="#d71f26"/></svg><span>View All Event</span></a>

<!-- instagram -->
<div class="media" style="left:28px;top:3505px;width:167px;height:105px;background:radial-gradient(ellipse at center,#c82a22 0%,rgba(200,42,34,.25) 55%,rgba(255,255,255,0) 72%)" role="img" aria-label="Red chili pepper with scattered flakes"></div>
<h2 class="display abs" style="left:152px;top:3662px;font-size:58px;line-height:64px">Follow Us<br><span class="hl">Instagram</span></h2>
<p class="copy abs" style="left:154px;top:3826px;width:460px">Stay connected with us on social media for daily updates, behind-the scenes moments, and exciting announcements.</p>
<div class="handle" style="top:3886px"><i></i>@BRISATOSTADA</div>
<div class="handle" style="top:3921px"><i></i>@NUEVOSENDERO</div>
<div class="media" style="left:600px;top:3595px;width:515px;height:435px;background:radial-gradient(ellipse at 50% 55%,#f1eadc 0%,#d8c9a6 40%,rgba(255,255,255,0) 72%)" role="img" aria-label="Two phones showing the brands' social media profiles"></div>
<div class="media" style="left:1045px;top:4060px;width:155px;height:110px;background:radial-gradient(circle at 30% 45%,#e2362a 0 30%,rgba(0,0,0,0) 31%),radial-gradient(circle at 80% 65%,#e8452f 0 28%,rgba(0,0,0,0) 29%)" role="img" aria-label="Sliced tomato halves"></div>

<!-- footer -->
<footer class="site-footer">
  <div class="abs" style="left:103px;top:55px;width:152px;height:215px;background:var(--white);border:2px solid var(--red);display:flex;flex-direction:column;align-items:center;padding-top:22px">
    <div style="font-weight:700;font-size:14px;color:var(--ink)">Brisa Tostada</div>
    <div style="width:64px;height:64px;background:var(--red);margin-top:22px"></div>
    <div style="width:80px;height:46px;background:#ececec;margin-top:22px"></div>
  </div>
  <h4 style="left:335px;top:76px">Contact Info</h4>
  <h4 style="left:335px;top:102px">Nuevo Sendero:</h4>
  <div class="item" style="left:335px;top:122px"><span class="pin">●</span> Pickup from 4182 Harlow Road<br>&nbsp;&nbsp;&nbsp;&nbsp;Today at 12:25 PM</div>
  <h4 style="left:335px;top:197px">Brisa Tostada:</h4>
  <div class="item" style="left:335px;top:217px"><span class="pin">●</span> 87 Linden Ave, Port Elm ON K9T 4B6<br><span class="pin">●</span> 1.555.013.2207<br><span class="pin">●</span> hello@brisatostada.com</div>
  <h4 style="left:634px;top:76px">Operating Hours</h4>
  <div class="item" style="left:634px;top:102px;font-size:12.5px">Monday to Friday: 9 AM – 9 PM<br>Saturday &amp; Sunday: 10 AM – 11 PM</div>
  <h4 style="left:907px;top:76px">Payment Opyions</h4>
  <div class="foot-rule" style="top:335px"></div>
  <div class="item" style="left:0;width:1200px;text-align:center;top:359px;font-size:12px">© COPYRIGHT BRISA TOSTADA, ALL RIGHTS RESERVED</div>
  <div class="item" style="left:987px;top:358px;font-size:14px;color:#fff;text-decoration:underline">Cookie Settings</div>
  <span class="abs" style="left:1131px;top:290px;width:44px;height:44px;border-radius:50%;background:var(--red);color:#fff;text-align:center;line-height:44px;font-size:14px">⌃</span>
</footer>
<div class="social"><span></span><span></span><span></span><span></span></div>
<div class="pay"><span></span><span></span><span></span><span></span><span></span><span></span><span></span><span></span><span></span></div>

</body>
</html>
```